Corvita-Nordal (Info Flyer for Workshops)

We need a flyer for an event (format A5, double-sided, portrait format). This event is aimed at lymphology experts (for example, pyhsiotherapists and lymphology therapists). The aim of these workshops is to create a quality circle. The logos of the flyer must be as follows: Page 1: with the text and the details of the logotype The logos for the Partners are thus attached below. The following design inputs: 1) The colors black and red (RGB Black: 0/0/0 // RGB Red: 227/0/11 2627) is the corporate color and must be integrated in the flyer. 2) The visual language should be applied to the theme of networking (No Go people, very much using graphical elements.) Please use the graphic element attached below (please use elements of the lymphology pathways, you can change the color into red or / and black. - do not use the whole Body contours (File: lymph2.psd)) 3) The company typeface is Univers LT Std. 4) The texts must be reader-friendly Please note this flyer is not created for Brellox, but for CorvitaNordal ,

```html
<!DOCTYPE html>
<html lang="fr">
<head>
<meta charset="utf-8">
<title>Corvita-Nordal – Cercle de qualité</title>
<link rel="stylesheet" href="https://fonts.googleapis.com/css2?family=Arimo:wght@400;700&family=Montserrat:wght@800&family=Saira+Semi+Condensed:wght@700&display=swap">
<style>
  :root {
    --red: #e3000b;
    --black: #000000;
    --white: #ffffff;
    --stage: #8f8f8f;
    --partner-ink: #333333;
  }
  * { margin: 0; padding: 0; box-sizing: border-box; }
  html, body { width: 1200px; height: 1200px; overflow: hidden; background: var(--stage); }
  .canvas { position: relative; width: 1200px; height: 1200px; }

  .page { position: absolute; top: 269px; width: 508px; height: 711px; background: var(--white); overflow: hidden; }
  .page--front { left: 64px; }
  .page--back { left: 620px; }

  /* front */
  .top-bar { position: absolute; left: 0; top: 0; width: 100%; height: 19px; background: var(--black); }
  .bottom-bar { position: absolute; left: 0; bottom: 0; width: 100%; height: 21px; background: var(--red); }
  .pathway-art { position: absolute; top: 19px; width: 110px; height: 420px;
    background: radial-gradient(ellipse at center, rgba(180,180,180,.28), rgba(255,255,255,0) 70%); }
  .pathway-art--left { left: 0; }
  .pathway-art--right { right: 0; }

  .brand { position: absolute; display: flex; align-items: center; gap: 8px;
    font-family: "Saira Semi Condensed", "Arial Narrow", sans-serif; font-weight: 700; line-height: .92; }
  .brand--front { left: 132px; top: 58px; color: var(--black); font-size: 46px; letter-spacing: 1px; }
  .brand--front .brand__mark { width: 40px; height: 86px; background: var(--black); }
  .brand--back { left: 18px; top: 26px; color: var(--white); font-size: 23px; letter-spacing: .5px; }
  .brand--back .brand__mark { width: 20px; height: 40px; background: var(--white); }

  .headline { position: absolute; left: 0; width: 100%; text-align: center;
    font-family: "Montserrat", sans-serif; font-weight: 800; line-height: 1; }
  .headline--cercle { top: 191px; font-size: 84px; color: var(--red); letter-spacing: 1px; }
  .headline--de { top: 271px; font-size: 84px; color: var(--red); }
  .headline--qualite { top: 351px; font-size: 84px; color: var(--black); letter-spacing: 1px; }

  .group-photo { position: absolute; left: 18px; top: 455px; width: 472px; height: 216px;
    background: linear-gradient(180deg, #3a3a44 0%, #2a2a33 55%, #cfcfd2 85%, #ffffff 100%); }
  .date-banner { position: absolute; left: 36px; top: 514px; width: 438px; height: 72px; background: var(--white);
    display: flex; align-items: center; justify-content: center;
    font-family: "Montserrat", sans-serif; font-weight: 800; font-size: 43px; color: var(--red); }

  /* back */
  .hero-photo { position: absolute; left: 0; top: 0; width: 100%; height: 312px;
    background: linear-gradient(120deg, #5a3540 0%, #a35a55 35%, #3a3b52 60%, #1f2a5a 80%, #d8d8dc 100%); }
  .hero-rule { position: absolute; left: 0; top: 312px; width: 100%; height: 6px; background: var(--black); }

  .details { position: absolute; left: 0; top: 318px; width: 100%; height: 248px;
    font-family: "Arimo", Arial, sans-serif; font-weight: 700; font-size: 13.5px; line-height: 16.5px; }
  .details__col { position: absolute; left: 0; top: 0; width: 115px; height: 100%; background: var(--red); }
  .details__row { position: absolute; left: 0; width: 100%; }
  .details__label { position: absolute; left: 24px; color: var(--white); }
  .details__value { position: absolute; left: 124px; width: 362px; color: #111; }

  .signup { position: absolute; left: 0; top: 566px; width: 100%; height: 64px; background: var(--black);
    color: var(--white); font-family: "Arimo", Arial, sans-serif; text-align: center; }
  .signup__main { margin-top: 13px; font-size: 16px; }
  .signup__main a { color: var(--red); text-decoration: none; font-weight: 700; }
  .signup__note { margin-top: 6px; font-size: 12.5px; }

  .partners { position: absolute; left: 0; top: 630px; width: 100%; height: 72px;
    background: linear-gradient(180deg, #ffffff, #ececec);
    display: flex; align-items: center; justify-content: space-around; padding: 0 18px;
    font-family: "Arimo", Arial, sans-serif; }
  .partner { font-size: 15px; font-weight: 700; color: var(--partner-ink); }
  .back-bar { position: absolute; left: 0; bottom: 0; width: 100%; height: 9px; background: var(--black); }
</style>
</head>
<body>
<main class="canvas">

  <section class="page page--front">
    <div class="top-bar"></div>
    <div class="pathway-art pathway-art--left" role="img" aria-label="Faint grey lymphatic pathway illustration"></div>
    <div class="pathway-art pathway-art--right" role="img" aria-label="Faint grey lymphatic pathway illustration"></div>

    <div class="brand brand--front">
      <span class="brand__mark"></span>
      <span>CORVITA-<br>NORDAL</span>
    </div>

    <h1 class="headline headline--cercle">CERCLE</h1>
    <p class="headline headline--de">DE</p>
    <p class="headline headline--qualite">QUALITÉ</p>

    <div class="group-photo" role="img" aria-label="Photo of a group of professionals standing in a row holding a banner"></div>
    <div class="date-banner">21 AVRIL 2018</div>
    <div class="bottom-bar"></div>
  </section>

  <section class="page page--back">
    <div class="hero-photo" role="img" aria-label="Photo of a speaker at a lectern with laptop facing a conference audience"></div>
    <div class="brand brand--back">
      <span class="brand__mark"></span>
      <span>CORVITA-<br>NORDAL</span>
    </div>
    <div class="hero-rule"></div>

    <div class="details">
      <div class="details__col"></div>
      <div class="details__row" style="top:12px"><span class="details__label">Date</span><span class="details__value">21 avril 2018</span></div>
      <div class="details__row" style="top:40px"><span class="details__label">Horaire</span><span class="details__value">9h00 -14h00</span></div>
      <div class="details__row" style="top:68px"><span class="details__label">Lieu</span><span class="details__value">Auditoire Marlen Voisard (PMF) CHRN, Lausanne</span></div>
      <div class="details__row" style="top:96px"><span class="details__label">Destinateur</span><span class="details__value">Physiothérapeutes, Lymphothérapeute</span></div>
      <div class="details__row" style="top:125px"><span class="details__label">Programme</span><span class="details__value">après une introduction sur les actualités dans la prise en charge des pathologies lymphatique nous organisons des ateliers pratique (drainage, bandage, compression élastique, les outils etc.)</span></div>
      <div class="details__row" style="top:201px"><span class="details__label">Prix</span><span class="details__value">CHF 100.-<br>CHF 50.- (pour les membres de CorvitaNordal)</span></div>
    </div>

    <div class="signup">
      <p class="signup__main">Inscription et renseignement via email : <a href="mailto:info@corvitanordal.ch">info@corvitanordal.ch</a></p>
      <p class="signup__note">Délai d’inscription : 15 mars 2018 (limitation de place, max 80 participants)</p>
    </div>

    <div class="partners">
      <span class="partner">Brellox</span>
      <span class="partner">Halvern &amp; Dorsch</span>
      <span class="partner">Velmora</span>
      <span class="partner">Ostrava medical</span>
    </div>
    <div class="back-bar"></div>
  </section>

</main>
</body>
</html>
```